out of the box Business Card Design for a Manufacturer / Distributor

We are a manufarturer and distributor of products.
the company name is VORTANI (Pic attached)

the picture is NOT a must have on the business Card.

the Business Card should look really professional and/or special, so out of the box thinking is welcome.

there should be 2 Adresses on the Business Card for Main and Branch Office.
Email Adress, homepage, Name is required
NO Phone Number

Our working field:
Private Labeling
high Quality Production
direct distribution
warehousing
trademark registration
legal support

Main Office:
Kornblumenweg 14
08352 Weidenthal
Germany

Branch Office:
Daska Lane
Rashidpur
Pakistan

Names:
Lukas Feldhaus (Owner)
Imran Qureshi (Owner)

Email:
lukas@vortani-example.com
imran@vortani-example.com

homepage:
vortani-example.com

Industry/Entity Type

Manufacturer Distributer

Contact Information for Business Card

Vortani

Requirements
Must have
• Names, both office Adresses, email, homepage
Should not have
• Phone Number

```html
<!DOCTYPE html>
<html lang="en">
<head>
<meta charset="utf-8">
<title>Vortani Business Card</title>
<link rel="stylesheet" href="https://fonts.googleapis.com/css2?family=Open+Sans:wght@400&family=Oswald:wght@300;400;600&display=swap">
<style>
  :root {
    --ink: #141824;
    --accent: #f99d2e;
    --paper: #ffffff;
    --text-light: #f2f2f2;
  }
  html, body {
    margin: 0;
    padding: 0;
    width: 1200px;
    height: 1200px;
    overflow: hidden;
    background: var(--paper);
  }
  .sheet { display: block; width: 1200px; height: 1200px; }
  .card-face { fill: var(--ink); }
  .band { fill: var(--accent); }
  .rule { fill: none; stroke: var(--accent); stroke-width: 3; }
  .brand-name {
    font-family: "Open Sans", Arial, sans-serif;
    font-weight: 400;
    font-size: 112px;
    fill: var(--paper);
    letter-spacing: 2px;
  }
  .web-address {
    font-family: "Open Sans", Arial, sans-serif;
    font-weight: 400;
    font-size: 34px;
    fill: var(--paper);
  }
  .owner-names {
    font-family: "Oswald", "Arial Narrow", sans-serif;
    font-weight: 600;
    font-size: 58px;
    fill: var(--text-light);
  }
  .contact-line {
    font-family: "Oswald", "Arial Narrow", sans-serif;
    font-weight: 300;
    font-size: 22px;
    fill: var(--paper);
  }
  .icon-fill { fill: var(--accent); }
  .icon-hole { fill: var(--ink); }
  .icon-stroke { fill: none; stroke: var(--accent); stroke-width: 4; stroke-linejoin: round; }
</style>
</head>
<body>
<svg class="sheet" viewBox="0 0 1932 1932" xmlns="http://www.w3.org/2000/svg">
  <!-- Front side -->
  <g class="card card-front">
    <rect class="card-face" x="397" y="135" width="1138" height="650"/>
    <polygon class="band" points="1241,176 1535,176 1535,239 1193,239"/>
    <polygon class="band" points="397,241 738,241 690,304 397,304"/>
    <polygon class="band" points="1241,618 1535,618 1535,681 1193,681"/>
    <polygon class="band" points="397,683 738,683 690,746 397,746"/>
    <text class="brand-name" x="966" y="507" text-anchor="middle">VORTANI</text>
    <text class="web-address" x="966" y="769" text-anchor="middle">WWW.VORTANI-EXAMPLE.COM</text>
  </g>

  <!-- Back side -->
  <g class="card card-back">
    <rect class="card-face" x="391" y="1126" width="1149" height="656"/>
    <polygon class="band" points="1244,1168 1540,1168 1540,1233 1197,1233"/>
    <polyline class="rule" points="391,1299 688,1299 736,1232 1197,1232"/>
    <text class="owner-names" x="740" y="1297" textLength="792" lengthAdjust="spacingAndGlyphs">LUKAS FELDHAUS &amp; IMRAN QURESHI</text>

    <g class="icon-pin">
      <path class="icon-fill" d="M498,1531 a20,20 0 0 1 20,20 c0,14 -20,32 -20,32 c0,0 -20,-18 -20,-32 a20,20 0 0 1 20,-20 z"/>
      <circle class="icon-hole" cx="498" cy="1550" r="7"/>
    </g>
    <text class="contact-line" x="548" y="1549">(MAIN OFF)Kornblumenweg 14, 08352 Weidenthal, Germany</text>
    <text class="contact-line" x="548" y="1577">(BRANCH OFF)Daska Lane, Rashidpur, Pakistan</text>

    <g class="icon-mail">
      <rect class="icon-stroke" x="476" y="1613" width="44" height="30" rx="3"/>
      <polyline class="icon-stroke" points="478,1616 498,1634 518,1616"/>
    </g>
    <text class="contact-line" x="548" y="1620">lukas@vortani-example.com</text>
    <text class="contact-line" x="548" y="1648">imran@vortani-example.com</text>

    <polyline class="rule" points="736,1679 1195,1679 1244,1612 1540,1612"/>
    <polygon class="band" points="391,1680 736,1680 688,1743 391,1743"/>
  </g>
</svg>
</body>
</html>
```